CONTEMPORARY Canva Art Design for Christians

I need a canvas art design on Christianity. The design must be in 3 SIMPLE dimensions: 12x 18 inches / 28 x 24 inches / 30 x 40 inches
The design must be accompanied by christian quote.
The christian quote can be "As For Me And My House We Will Serve The Lord (Joshua 24:15)" or any other quote that is good for display in a christian home.

I DON'T WANT THE TRADITIONAL CHRISTIAN DESIGN.. I WANT COLOURFUL, MEANINGFUL and CONTEMPORARY, MODERN DESIGN. And stay away from the scary image of Jesus in dark background, it only makes the home more scary not holy!

Target Market(s)

Christians

Colors

Designer to choose colors to be used in the design.

Requirements
Must have
• A graphic design and a christian quote that is powerful and edifies the soul. Great for display at home. Great use of colours to enhance the message.
Nice to have
• I wish to see great unique design with strong use of colours, images to enhance the scripture. It must glorify Jesus.
Should not have
• Should not be dull.

```html
<!DOCTYPE html>
<html lang="en">
<head>
<meta charset="utf-8">
<title>As for Me and My House – Joshua 24:15</title>
<link rel="stylesheet" href="https://fonts.googleapis.com/css2?family=Pinyon+Script&family=Cormorant+Garamond:wght@500&family=Damion&family=Kaushan+Script&family=Montserrat:wght@500;800&display=swap">
<style>
  :root {
    --wood-dark: #8a5418;
    --wood-mid: #a9691f;
    --wood-light: #b87a2c;
    --paper: #d8c3a1;
    --paper-edge: #f8f0e0;
    --ink-white: #ffffff;
    --ink-gold: #f4ee9c;
    --ink-brown: #4d2f17;
    --motif-tone: #8f5a24;
  }
  html, body {
    margin: 0;
    padding: 0;
    width: 1200px;
    height: 800px;
    overflow: hidden;
    background: #ffffff;
  }
  .artwork {
    display: block;
    width: 1200px;
    height: 800px;
  }
  .script-ornate { font-family: "Pinyon Script", cursive; fill: var(--ink-white); }
  .serif-line { font-family: "Cormorant Garamond", serif; font-weight: 500; fill: var(--ink-white); }
  .script-house { font-family: "Damion", "Kaushan Script", cursive; fill: var(--ink-white); }
  .script-serve { font-family: "Damion", "Kaushan Script", cursive; fill: var(--ink-gold); }
  .script-hand { font-family: "Kaushan Script", cursive; fill: var(--ink-white); }
  .sans-heavy { font-family: "Montserrat", sans-serif; font-weight: 800; fill: var(--ink-white); }
  .reference { font-family: "Montserrat", sans-serif; font-weight: 500; fill: var(--ink-brown); }
</style>
</head>
<body>
<svg class="artwork" viewBox="0 0 1200 800" xmlns="http://www.w3.org/2000/svg">
  <defs>
    <linearGradient id="wood-tone" x1="0" y1="0" x2="1" y2="0">
      <stop offset="0" stop-color="var(--wood-mid)"/>
      <stop offset="0.35" stop-color="var(--wood-light)"/>
      <stop offset="0.7" stop-color="var(--wood-mid)"/>
      <stop offset="1" stop-color="var(--wood-dark)"/>
    </linearGradient>
    <radialGradient id="motif-glow" cx="0.5" cy="0.55" r="0.5">
      <stop offset="0" stop-color="var(--motif-tone)" stop-opacity="0.45"/>
      <stop offset="1" stop-color="var(--motif-tone)" stop-opacity="0"/>
    </radialGradient>
  </defs>

  <rect class="wood-panel" role="img" aria-label="Warm brown wood grain backdrop" width="1200" height="800" fill="url(#wood-tone)"/>

  <rect class="house-motif" role="img" aria-label="Faint house roof motif" x="780" y="30" width="410" height="250" rx="60" fill="url(#motif-glow)"/>

  <g class="quote">
    <text class="script-ornate" x="50" y="182" font-size="180">A</text>
    <text class="serif-line" x="206" y="172" font-size="92" textLength="572" lengthAdjust="spacingAndGlyphs">s for me &amp; my</text>
    <text class="script-house" x="272" y="402" font-size="176" textLength="400" lengthAdjust="spacingAndGlyphs">House,</text>
    <text class="script-hand" x="722" y="392" font-size="60" textLength="218" lengthAdjust="spacingAndGlyphs">we will</text>
    <text class="script-serve" x="100" y="574" font-size="168" textLength="390" lengthAdjust="spacingAndGlyphs">Serve</text>
    <text class="script-hand" x="530" y="568" font-size="96" textLength="158" lengthAdjust="spacingAndGlyphs">the</text>
    <text class="sans-heavy" x="706" y="577" font-size="134" textLength="410" lengthAdjust="spacingAndGlyphs">LORD</text>
  </g>

  <g class="torn-paper">
    <polygon fill="var(--paper-edge)" points="0,678 30,672 60,680 95,664 120,668 150,650 180,660 215,648 240,666 270,654 300,664 330,640 360,656 395,646 420,660 455,650 480,668 510,660 540,672 575,662 600,676 640,666 680,672 715,660 750,668 790,658 820,664 850,648 880,656 910,642 940,650 975,638 1000,652 1030,640 1060,650 1090,636 1120,646 1150,630 1175,640 1200,628 1200,800 0,800"/>
    <polygon fill="var(--paper)" points="0,688 35,684 70,690 100,676 130,680 160,662 190,672 220,660 250,676 280,666 310,676 340,652 370,668 400,658 430,672 460,662 490,680 520,672 550,682 580,674 610,686 650,676 690,682 720,672 760,678 800,668 830,674 860,660 890,666 920,654 950,662 980,650 1010,664 1040,652 1070,662 1100,648 1130,658 1160,642 1185,652 1200,640 1200,800 0,800"/>
    <text class="reference" x="726" y="764" font-size="54">Joshua 24:15</text>
  </g>
</svg>
</body>
</html>
```